Logo and Web site for a boutique IT/Tech company

We are a small boutique IT and software company based in Cape Town, South Africa called Velmora. We cater to startups & medium sized businesses and provide end-to-end services to manage entire IT departments. We've got highly skilled staff who have worked for Zenith 400 companies previously, are contributors to open source projects and have been part of several startups. What sets us apart is our experience in executing end-to-end projects as well as our in-depth technical knowledge. Our products and services include:

1. Custom software development
2. Product management
3. Infrastructure
4. Security
5. Training & Mentoring

We are looking for a creative designer to:

1. Create a swanky tech logo for us

The logo should inspire, give a very creative tech feel (code, commits, debuggers etc.) and must give a feeling of cloud, AI, Robotics, block chain, augmented reality and any new/emerging tech. However, it must remain simple, elegant and authoritative. Velmora in itself does not mean anything. It was an error at the companies registration office that led to this name.

2. Create a new website for us:

Website objectives: The primary objective of the website is to generate business leads. The design must communicate an extremely professional and succinct message to visitors, compelling them to believe in our ability to deliver.

Navigation structure: This will be left to the designer. I am looking for clean, professional and minimalist design. There should be minimal clicking and navigation, parallax/storytelling can be incorporated. In a nutshell, the aim is to pack as much as possible on the main page, without making it look cluttered.

Website features:
1. Top priorities:
a. What we do. Must showcase our products/services offering to quickly match what prospective clients are looking for.
b. Why us: Once the customer/potential knows that we offer the services they are looking for, we need to re-enforce that we can deliver the services they seek. We re-enforce this by providing a section which pitches to customers why they must choose us. In addition to some bulleted point, this will highlight our projects on CodeHarbor or Gigsmith (point number 2 below) to highlight what we've delivered in past (refer to the attached document).
b. Allow customers to quickly and easily contact us/submit a query at any point from the moment they land on the to home page. This form should be available at all times, and should be titled "What are you looking for?". The following fields are required in the form: first and foremost a text area to capture what the customer is looking for, a text field for budget, name, mobile number and email address.
c. "Hire us Gigsmith" link
2. Priority 2: The main page should also have a section showcasing/summarizing our projects on CodeHarbor. Clicking on this should take the user to the CodeHarbor repo.
3. Priority 3: The front page must also have a page to showcase our existing clients and testimonials (logos)
4. Priority 4: The front page must have a place to showcase our partnerships with vendors such as QCP, Nimbra, GeoLoom etc.
5. Priority 5: The front page must have a team section that has a photo/avatar and one liner profile (e.g. Full stack dev) for each team member.
a. Clicking on the team members' profile should take the user to the team member's blog.
b. A blog page for each team member with sections to show avatar, information from the team member's QueryPile profile, Tweets on Chirplet and CodeHarbor repo/commits.
5. Priority 5: Must provide a section to showcase/highlight the tech stacks we work with e.g. Stratum, Brewlang, NodeJS, etc.
6. Priority 6: Must provide a gallery section to display images of events/office setting/brain storming sessions/clients/employees etc.

Other requirements:
1. The designer must also figure out a way to showcase the CEO's blog on the front page. Bonus - if you are able to have a feed for other team members blog on the main page as well.
2. Please include a ticker/banner on the main page for company announcements - clicking here should take the reader to a new/announcements page with details.

Websites I like: I will not mention any. Don't want to anchor :-)

**Please note**: If you don't understand a requirement or have questions, please feel free to message and ask a question. Please don't make assumptions!

Target Market(s)

There are two distinct groups we are trying to reach out to, hence the design needs to appeal to both:
1. Startups looking for mature and experienced tech partners to help plan, develop, launch and manage their ideas and products. The design must ooze a cutting edge feel. As much as these startups are looking for cutting edge skills, they are also looking for experience and maturity. The design must strike a good balance between the two.
2. Small to medium sized businesses looking for an IT partner (desktop support, network, email, antivirus, backups, telephony, custom applications etc.)

Industry/Entity Type

It Service

Contact Information for Business Card

The business card must be simple and uber professional. We are open to suggestions and ideas but have the following in mind:
1. A profile picture
2. Name and contact details of of the organization
3. Name of the person along with designation
4. Contact details for the person
4. Products/services offered by organization

If you have any ideas/suggestions or questions, feel free to contact us instead of making assumptions on your own.

Logo Text

VELMORA

Coding

Coded - Design and coding required

Number of Pages Required

5+ page

Font styles to use
Sans Serif

Colors

Designer to choose colors to be used in the design.

Requirements
Must have
• EDIT: We'd prefer designs that use/allow parallax and fit everything in single page.
• 1. Design for the main/landing page.
• 2. Design for the blog page for team members (priority 5 in main description)
• 3. Design for a details page for the products/services e.g. When the user clicks on any of the products/services listed on the main page, there should be a page/view to show the details. The details page should provide a structured way to show:
• a. Details/description about the product/service
• b. A section to describe how do we approach/deliver that product service
• c. List of clients with a brief description for services rendered to them along with testimonials.
• 4. Design of details page for the tech stacks
• 5. A news/announcements page that contains all announcements
• 6. An about us page containing information about the company, contact information with map etc.
• 7. Design a codeharbor page to summarize/display our projects. This is a one pager similar to http://plorvex.codeharbor-example.io/ or https://openlab.trevamind-example.com/. Does not have to contain much graphics etc. but just a simple listing with monthly charts per codeharbor repo (Similar to http://pkg-tally-example.org/#/zephyr-kit-phone-field).
Nice to have
• Parallax/Story telling
Should not have
• Clutter and clumsy look

```html
<!DOCTYPE html>
<html lang="en">
<head>
<meta charset="utf-8">
<title>Velmora – IT and software company</title>
<link rel="stylesheet" href="https://fonts.googleapis.com/css2?family=Poppins:wght@500;600;700&family=Quicksand:wght@400;500;600;700&display=swap">
<style>
:root{
  --blue:#0f8fcf;
  --cyan:#1cc3dc;
  --aqua:#07d6d8;
  --ink:#333a40;
  --text:#55595e;
  --muted:#8a8f94;
  --line:#dcdfe2;
  --paper:#ffffff;
  --mist:#f1f2f3;
  --night:#2f3133;
}
*{box-sizing:border-box;margin:0;padding:0}
html,body{width:1200px;height:4380px;overflow:hidden}
body{font-family:"Quicksand",sans-serif;color:var(--text);background:var(--paper);position:relative}
section,header,footer{position:absolute;left:0;width:1200px}
.abs{position:absolute}
h2.section-title{position:absolute;left:0;width:100%;text-align:center;font-family:"Poppins",sans-serif;font-weight:600;font-size:40px;color:var(--blue);line-height:1}
h2.section-title span{color:var(--cyan)}
.light-title,.light-title span{color:#fff!important}

/* header */
.site-header{top:0;height:170px;background:var(--paper)}
.brand{left:79px;top:30px;display:flex;align-items:center;gap:12px}
.brand-mark{width:36px;height:36px;background:var(--cyan);border-radius:6px}
.brand-name{font-weight:700;font-size:44px;color:var(--blue);line-height:1}
.social{left:735px;top:42px;display:flex;gap:14px}
.social span{width:36px;height:36px;border-radius:50%;border:1px solid var(--line);display:flex;align-items:center;justify-content:center;font-size:14px;font-weight:700;color:var(--ink)}
.cta{left:946px;top:38px;width:175px;height:46px;background:var(--blue);color:#fff;font-weight:700;font-size:15px;display:flex;align-items:center;justify-content:center;letter-spacing:.5px}
.main-nav{left:0;top:117px;width:1200px;height:53px;border-top:1px solid var(--line);border-bottom:1px solid var(--line)}
.main-nav a{position:absolute;top:15px;font-size:15px;font-weight:600;color:var(--ink);text-decoration:none;letter-spacing:.3px}
.main-nav a.active{color:var(--blue);border-bottom:3px solid var(--blue);padding-bottom:12px}

/* hero */
.hero{top:170px;height:580px;
  background:
    radial-gradient(ellipse 420px 360px at 860px 260px,rgba(28,34,42,.85),rgba(28,34,42,0) 70%),
    radial-gradient(ellipse 500px 200px at 260px 520px,rgba(200,206,212,.55),rgba(200,206,212,0) 70%),
    linear-gradient(115deg,#9aa1a7 0%,#6e767d 35%,#4a5259 65%,#3a4148 100%)}
.hero h1{position:absolute;left:79px;top:205px;font-family:"Poppins",sans-serif;font-weight:600;font-size:60px;line-height:74px;color:#fff}

/* services */
.services{top:750px;height:754px;background:var(--paper)}
.service{position:absolute;width:320px;text-align:center}
.service .icon{width:86px;height:86px;border-radius:50%;background:var(--blue);margin:0 auto 22px;display:flex;align-items:center;justify-content:center}
.service h3{font-weight:600;font-size:21px;color:var(--ink);line-height:26px;margin-bottom:6px}
.service p{font-size:14px;line-height:23px;color:var(--muted);padding:0 16px}
.service .more{display:inline-block;margin-top:10px;font-size:13px;font-weight:700;color:var(--ink);text-decoration:underline}

/* why us */
.why{top:1504px;height:373px;background:var(--mist)}
.why h2{position:absolute;left:79px;top:87px;font-family:"Poppins",sans-serif;font-weight:600;font-size:40px;color:var(--blue)}
.why h2 span{color:var(--cyan)}
.why ul{position:absolute;left:79px;top:140px;width:420px;list-style:none}
.why li{position:relative;padding-left:32px;font-size:14px;line-height:22px;color:var(--text);margin-bottom:16px}
.why li::before{content:"";position:absolute;left:0;top:6px;width:11px;height:11px;border-radius:50%;background:var(--blue)}
.why-frame{left:704px;top:49px;width:420px;height:263px;background:#fff;border:2px solid var(--line);border-radius:14px}
.why-photo{position:absolute;left:44px;top:14px;width:332px;height:231px;
  background:
    radial-gradient(ellipse 140px 90px at 240px 70px,rgba(72,110,168,.55),rgba(72,110,168,0) 70%),
    radial-gradient(ellipse 160px 60px at 160px 200px,rgba(60,62,66,.7),rgba(60,62,66,0) 70%),
    linear-gradient(135deg,#eef1f4,#cdd6de 55%,#9aa6b1)}

/* stacks */
.stacks{top:1877px;height:423px;background:var(--paper)}
.stack{position:absolute;width:184px;height:104px;border:1px solid var(--line);display:flex;align-items:center;justify-content:center;font-weight:700;font-size:26px;color:var(--ink);gap:8px}
.stack i{display:block;width:14px;height:14px;background:var(--blue)}

/* team */
.team{top:2300px;height:556px;background:linear-gradient(120deg,#1587d6 0%,#0fb3de 55%,#06dbd8 100%)}
.member{position:absolute;top:120px;width:240px;height:336px;background:#fff}
.member .photo{height:242px}
.photo.tone-a{background:
  radial-gradient(ellipse 90px 120px at 120px 110px,rgba(224,186,160,.9),rgba(224,186,160,0) 75%),
  linear-gradient(180deg,#6a4a3a 0%,#8d6a58 45%,#d9c7bb 100%)}
.photo.tone-b{background:
  radial-gradient(ellipse 80px 100px at 120px 95px,rgba(226,196,176,.9),rgba(226,196,176,0) 75%),
  linear-gradient(180deg,#f4f4f4 0%,#e6e6e6 50%,#c9d3de 100%)}
.member h4{text-align:center;margin-top:20px;font-weight:600;font-size:17px;color:var(--ink)}
.member p{text-align:center;font-size:13px;color:var(--muted);margin-top:8px}
.dots{position:absolute;left:0;width:100%;display:flex;justify-content:center;gap:6px}
.dots i{display:block;width:34px;height:4px;border-radius:2px;background:rgba(255,255,255,.5)}
.dots i.on{background:#fff}
.dots.dark i{background:#cfd3d6}
.dots.dark i.on{background:var(--cyan)}

/* testimonials */
.testimonials{top:2856px;height:449px;background:var(--paper)}
.client-badge{left:490px;top:128px;width:220px;height:91px;border:1px solid var(--line);display:flex;align-items:center;justify-content:center;gap:10px;font-weight:700;font-size:38px;color:var(--ink)}
.client-badge i{display:block;width:22px;height:22px;background:#d3222a}
.quote{left:181px;top:253px;width:841px;text-align:center;font-size:14px;line-height:23px;color:var(--text)}
.quote-by{left:0;top:354px;width:100%;text-align:center;font-size:17px;color:var(--text)}
.arrow{top:210px;width:41px;height:82px;background:#595d61;display:flex;align-items:center;justify-content:center}

/* projects */
.projects{top:3305px;height:447px;background:var(--mist)}
.project{position:absolute;top:120px;width:324px;height:240px}
.project.tablet{background:
  radial-gradient(ellipse 120px 70px at 190px 120px,rgba(150,110,80,.7),rgba(150,110,80,0) 75%),
  linear-gradient(135deg,#f4f1ec 0%,#d8cbbb 45%,#8c7662 100%)}
.project.office{background:linear-gradient(135deg,#b9d6e4,#6fa7c4)}
.project.laptop{background:
  radial-gradient(ellipse 140px 80px at 170px 150px,rgba(236,232,228,.8),rgba(236,232,228,0) 75%),
  linear-gradient(135deg,#cfc6bf 0%,#8a7d74 55%,#4e4540 100%)}
.project-label{position:absolute;inset:0;background:rgba(12,200,220,.72);display:flex;flex-direction:column;align-items:center;justify-content:center;color:#fff;font-weight:700;font-size:24px;gap:10px}

/* contact */
.contact{top:3752px;height:345px;background:linear-gradient(100deg,#06c2dc 0%,#07d7d9 60%,#09e3d4 100%)}
.field{position:absolute;border:1px solid rgba(255,255,255,.75);color:#fff;font-size:14px;padding:8px 12px;background:rgba(255,255,255,.05)}
.submit{position:absolute;left:610px;top:234px;width:365px;height:41px;background:#fff;color:var(--cyan);font-weight:700;font-size:17px;display:flex;align-items:center;justify-content:center;letter-spacing:.5px}

/* footer */
.site-footer{top:4097px;height:283px;background:var(--night);color:#fff}
.footer-brand{left:0;top:82px;width:100%;display:flex;justify-content:center;align-items:center;gap:12px}
.footer-brand i{display:block;width:34px;height:34px;border-radius:50%;background:var(--blue)}
.footer-brand b{font-size:40px;font-weight:700;color:var(--blue)}
.footer-nav{left:0;top:197px;width:100%;display:flex;justify-content:center;gap:44px;font-size:15px;font-weight:600}
.copyright{left:0;top:236px;width:100%;text-align:center;font-size:14px}
</style>
</head>
<body>

<header class="site-header">
  <div class="brand abs"><i class="brand-mark"></i><span class="brand-name">Velmora</span></div>
  <div class="social abs">
    <span aria-label="Kinfolk">K</span>
    <span aria-label="Chirplet">C</span>
    <span aria-label="Orbitly">O</span>
    <span aria-label="Careerloop">L</span>
  </div>
  <a class="cta abs">CONTACT NOW</a>
  <nav class="main-nav abs">
    <a class="active" style="left:79px">HOME</a>
    <a style="left:166px">ABOUT US</a>
    <a style="left:283px">SERVICES</a>
    <a style="left:394px">WHY US</a>
    <a style="left:496px">CONTACT</a>
  </nav>
</header>

<section class="hero" role="img" aria-label="Photo of a developer working at a desk in a busy office">
  <h1>IT and software<br>company</h1>
</section>

<section class="services">
  <h2 class="section-title" style="top:55px">What <span>We Do</span></h2>
  <div class="service" style="left:80px;top:132px">
    <div class="icon"><svg width="40" height="40" viewBox="0 0 40 40" fill="none" stroke="#fff" stroke-width="2.5"><rect x="5" y="9" width="30" height="20" rx="2"/><path d="M16 16l-4 3 4 3M24 16l4 3-4 3M14 34h12"/></svg></div>
    <h3>Custom application<br>development</h3>
    <p>Lorem Ipsum is simply dummy text of the printing and typesetting industry.</p>
    <span class="more">READ MORE</span>
  </div>
  <div class="service" style="left:440px;top:132px">
    <div class="icon"><svg width="40" height="40" viewBox="0 0 40 40" fill="none" stroke="#fff" stroke-width="2.5"><rect x="8" y="6" width="24" height="28" rx="3"/><path d="M14 14h12M14 20h12M14 26h7"/></svg></div>
    <h3>Product management</h3>
    <p>Lorem Ipsum is simply dummy text of the printing and typesetting industry. Lorem Ipsum has been the industry's.</p>
    <span class="more">READ MORE</span>
  </div>
  <div class="service" style="left:800px;top:132px">
    <div class="icon"><svg width="40" height="40" viewBox="0 0 40 40" fill="none" stroke="#fff" stroke-width="2.5"><rect x="5" y="8" width="30" height="20" rx="2"/><path d="M15 34h10M20 28v6M14 20l4-4 4 3 5-5"/></svg></div>
    <h3>Infrastructure management</h3>
    <p>Lorem Ipsum is simply dummy text of the printing and typesetting industry. Lorem Ipsum has been the industry's.</p>
    <span class="more">READ MORE</span>
  </div>
  <div class="service" style="left:258px;top:436px">
    <div class="icon"><svg width="40" height="40" viewBox="0 0 40 40" fill="none" stroke="#fff" stroke-width="2.5"><path d="M20 5l12 5v9c0 8-5 13-12 16C13 32 8 27 8 19v-9z"/><rect x="15" y="18" width="10" height="8"/><path d="M17 18v-3a3 3 0 016 0v3"/></svg></div>
    <h3>Security</h3>
    <p>Lorem Ipsum is simply dummy text of the printing and typesetting industry. Lorem Ipsum has been the industry's.</p>
    <span class="more">READ MORE</span>
  </div>
  <div class="service" style="left:617px;top:436px">
    <div class="icon"><svg width="40" height="40" viewBox="0 0 40 40" fill="none" stroke="#fff" stroke-width="2.5"><rect x="7" y="8" width="26" height="16" rx="1"/><circle cx="13" cy="30" r="3"/><circle cx="27" cy="30" r="3"/><path d="M12 19l5-5 4 3 6-5"/></svg></div>
    <h3>Training &amp; Mentoring</h3>
    <p>Lorem Ipsum is simply dummy text of the printing and typesetting industry. Lorem Ipsum has been the industry's.</p>
    <span class="more">READ MORE</span>
  </div>
</section>

<section class="why">
  <h2>Why <span>us</span></h2>
  <ul>
    <li>Action speaks louder than words – checkout download stats for our popular projects from Pakkit</li>
    <li>Get the benefits of lean entrepreneurial team, without the risks</li>
    <li>We treat your business as ours – your loss is our loss</li>
    <li>We keep it real – no "mono roll" or "success theaters"</li>
  </ul>
  <div class="why-frame abs">
    <div class="why-photo" role="img" aria-label="Photo of a team reviewing charts on a laptop"></div>
  </div>
</section>

<section class="stacks">
  <h2 class="section-title" style="top:58px">Stacks That <span>We Work With</span></h2>
  <div class="stack" style="left:79px;top:106px">Flintic</div>
  <div class="stack" style="left:292px;top:106px"><i></i>Stratum</div>
  <div class="stack" style="left:505px;top:106px">Cargoly</div>
  <div class="stack" style="left:721px;top:106px">Brewlang</div>
  <div class="stack" style="left:934px;top:106px"><i></i>Nimbra</div>
  <div class="stack" style="left:79px;top:237px">QCP</div>
  <div class="stack" style="left:292px;top:237px">Pageforge</div>
  <div class="stack" style="left:505px;top:237px">Vertexa</div>
  <div class="stack" style="left:721px;top:237px">Ledgera</div>
  <div class="stack" style="left:934px;top:237px"><i></i>Trigona</div>
</section>

<section class="team">
  <h2 class="section-title light-title" style="top:60px">Stacks That We Work With</h2>
  <div class="member" style="left:79px"><div class="photo tone-a" role="img" aria-label="Portrait photo of a team member"></div><h4>Surname Name</h4><p>Lorem Ipsum is simply.</p></div>
  <div class="member" style="left:348px"><div class="photo tone-b" role="img" aria-label="Portrait photo of a team member"></div><h4>Surname Name</h4><p>Lorem Ipsum is simply.</p></div>
  <div class="member" style="left:617px"><div class="photo tone-a" role="img" aria-label="Portrait photo of a team member"></div><h4>Surname Name</h4><p>Lorem Ipsum is simply.</p></div>
  <div class="member" style="left:885px"><div class="photo tone-b" role="img" aria-label="Portrait photo of a team member"></div><h4>Surname Name</h4><p>Lorem Ipsum is simply.</p></div>
  <div class="dots" style="top:490px"><i class="on"></i><i></i></div>
</section>

<section class="testimonials">
  <h2 class="section-title" style="top:52px">Our <span>Testimonials</span></h2>
  <div class="client-badge abs"><i></i>Stratum</div>
  <p class="quote abs">Lorem Ipsum is simply dummy text of the printing and typesetting industry. Lorem Ipsum has been the industry's standard dummy text ever since the 1500s, when an unknown printer took a galley of type and scrambled it to make a type specimen book. It has survived not only five centuries, but also the leap into electronic typesetting.</p>
  <p class="quote-by abs">- Lorem Ipsum is simply.</p>
  <div class="arrow abs" style="left:35px"><svg width="14" height="24" viewBox="0 0 14 24" fill="none" stroke="#fff" stroke-width="2"><path d="M12 2L2 12l10 10"/></svg></div>
  <div class="arrow abs" style="left:1124px"><svg width="14" height="24" viewBox="0 0 14 24" fill="none" stroke="#fff" stroke-width="2"><path d="M2 2l10 10-10 10"/></svg></div>
</section>

<section class="projects">
  <h2 class="section-title" style="top:52px">Our <span>Projects</span></h2>
  <div class="project tablet" style="left:79px" role="img" aria-label="Photo of hands using a tablet"></div>
  <div class="project office" style="left:438px" role="img" aria-label="Photo of an office workspace">
    <div class="project-label">Project Name
      <svg width="34" height="34" viewBox="0 0 34 34" fill="none" stroke="#fff" stroke-width="3"><path d="M14 20l6-6"/><path d="M12 16l-4 4a4.5 4.5 0 006 6l4-4M22 18l4-4a4.5 4.5 0 00-6-6l-4 4"/></svg>
    </div>
  </div>
  <div class="project laptop" style="left:797px" role="img" aria-label="Photo of hands typing on a laptop"></div>
  <div class="dots dark" style="top:420px"><i class="on"></i><i></i></div>
</section>

<section class="contact">
  <h2 class="section-title light-title" style="top:64px">Contact Us</h2>
  <div class="field" style="left:225px;top:132px;width:365px;height:41px">Name</div>
  <div class="field" style="left:225px;top:183px;width:365px;height:41px">Email</div>
  <div class="field" style="left:225px;top:234px;width:365px;height:41px">Phone</div>
  <div class="field" style="left:610px;top:132px;width:365px;height:92px">Message</div>
  <div class="submit">SUBMIT</div>
</section>

<footer class="site-footer">
  <div class="footer-brand abs"><i></i><b>Velmora</b></div>
  <nav class="footer-nav abs"><span>Home</span><span>About Us</span><span>Services</span><span>Why Us</span><span>Contact</span></nav>
  <p class="copyright abs">©Velmora software company. 2018 - All Rights Reserved.</p>
</footer>

</body>
</html>
```